Power point presentation optimization, in terms of content design

I have a completed business presentation, with all the texting, but I need some design improvement in terms of text formatting, lettering, text boxes, arrows, bullets, shapes and their formatting, relative location of text boxes and pictures in the slide, etc, etc, so that this specific presentation becomes more visually appealing.
Our company power point template is available.
I´m providing our company power point template (to be used as a reference) as well as the presentation that needs to be improved.

Target Market(s)

Potential partner in business.

Industry/Entity Type

Health

Requirements
Nice to have
• More ellegant collors (more according to the template) on the picture of slide 7. A more elegant dollar image (slide 16).

```html
<!DOCTYPE html>
<html lang="pt">
<head>
<meta charset="utf-8">
<title>Centro de Telemedicina – Apresentação</title>
<link href="https://fonts.googleapis.com/css2?family=Poppins:wght@400;500;600;700;800&display=swap" rel="stylesheet">
<style>
:root{
  --page:#e3e4e6;
  --navy:#1e3a6b;
  --teal:#3580aa;
  --teal-btn:#3a85ae;
  --ink:#2a2a2a;
  --dark:#121416;
  --white:#ffffff;
}
*{margin:0;padding:0;box-sizing:border-box}
html,body{width:1200px;height:4231px;overflow:hidden;background:var(--page);font-family:'Poppins',sans-serif;color:var(--ink)}
.slide{position:absolute;left:36px;width:1128px;height:635px;overflow:hidden;box-shadow:0 2px 6px rgba(0,0,0,.25)}
.abs{position:absolute}

/* cover */
.cover{top:64px;background:linear-gradient(160deg,#2a3440 0%,#1a2029 50%,#0f1318 100%)}
.cover .brand{left:0;right:0;top:50px;display:flex;justify-content:center;align-items:center;gap:12px;color:var(--white);font-weight:700;font-size:22px;text-transform:uppercase;letter-spacing:.5px}
.cover .brand-mark{width:38px;height:38px;border:3px solid var(--white)}
.cover h1{left:0;right:0;top:250px;text-align:center;color:var(--white);font-weight:700;font-size:42px;line-height:60px}

/* about */
.about{top:757px;background:var(--white)}
.about h2{left:0;right:0;top:30px;text-align:center;color:var(--navy);font-weight:800;font-size:50px}
.about .intro{left:130px;width:868px;top:128px;text-align:center;font-size:14px;line-height:26px;color:#444}
.about .intro p+p{margin-top:8px}
.about .diagram{left:161px;top:308px;width:330px;height:282px;border-radius:50%/40%;background:radial-gradient(ellipse at center,#c9d7ef 0%,#e9eef7 70%,#ffffff 100%)}
.btn{left:627px;width:335px;height:70px;border-radius:20px;display:flex;align-items:center;justify-content:center;color:var(--white);font-size:16px;font-weight:500}
.btn.teal{background:var(--teal-btn)}
.btn.navy{background:var(--navy)}

/* profile */
.profile{top:1450px;background:var(--white)}
.profile .panel{left:565px;top:0;width:563px;height:635px;background:var(--teal)}
.profile .portrait{left:694px;top:28px;width:312px;height:607px;border-radius:140px 140px 0 0;background:linear-gradient(180deg,#4a4f58 0%,#23262c 60%,#15171a 100%)}
.profile h2{left:32px;top:70px;color:var(--navy);font-weight:800;font-size:48px}
.profile h3{position:absolute;left:30px;font-size:21px;font-weight:600;color:#222}
.profile .bio{position:absolute;left:31px;width:510px;font-size:11.5px;line-height:24px;color:#333}

/* services */
.services{top:2142px;background:linear-gradient(180deg,#1c1f23 0%,#0e1012 100%)}
.services h2{left:0;right:0;top:30px;text-align:center;color:var(--white);font-weight:800;font-size:58px}
.card{position:absolute;width:272px;height:157px;border:1.5px solid rgba(255,255,255,.85);border-radius:18px;display:flex;align-items:center;justify-content:center;text-align:center;padding:30px 20px 0;color:var(--white);font-weight:700;font-size:17px;line-height:26px}
.card .num{position:absolute;left:50%;top:-36px;margin-left:-36px;width:72px;height:72px;border-radius:50%;background:var(--teal-btn);border:5px solid #15181b;outline:1.5px solid rgba(255,255,255,.85);display:flex;align-items:center;justify-content:center;font-size:26px;font-weight:700}

/* costs */
.costs{top:2835px;background:var(--white)}
.costs .dots{width:124px;height:64px;background:#f0f1f3}
.costs .band{left:0;top:119px;width:565px;height:86px;background:var(--teal);display:flex;align-items:center;justify-content:center;color:var(--white);font-size:28px;font-weight:700}
.costs ul{position:absolute;left:34px;top:240px;width:510px;list-style:none;font-size:13.5px;line-height:39px;color:#333}
.costs li{position:relative;padding-left:20px}
.costs li svg{position:absolute;left:0;top:13px}
.costs .photo{left:565px;top:0;width:563px;height:635px;background:linear-gradient(135deg,#dfe3e6 0%,#a9b2b8 45%,#3a3f45 100%)}

/* closing */
.closing{top:3528px;background:linear-gradient(160deg,#24282d 0%,#101214 100%)}
.closing .frame{left:404px;top:52px;width:684px;height:533px;border:2px solid var(--white)}
.closing h2{left:628px;top:278px;color:var(--white);font-weight:800;font-size:64px}
.closing .ring{left:90px;top:76px;width:508px;height:508px;border-radius:50%;border:2px solid var(--white)}
.closing .photo{left:108px;top:94px;width:472px;height:472px;border-radius:50%;background:radial-gradient(circle at 50% 40%,#f3f1ee 0%,#d8dde2 60%,#9aa4ae 100%)}
</style>
</head>
<body>

<section class="slide cover">
  <div class="abs" role="img" aria-label="Radiologistas a analisar exames em múltiplos monitores" style="inset:0;background:linear-gradient(180deg,rgba(60,90,120,.25),rgba(0,0,0,.35))"></div>
  <div class="abs brand"><span class="brand-mark"></span>Centro de Telemedicina</div>
  <h1 class="abs">Centro de Telemedicina<br>Uma perspetiva de 5 minutos</h1>
</section>

<section class="slide about">
  <h2 class="abs">SOBRE NÓS</h2>
  <div class="abs intro">
    <p>O Centro Internacional de Telemedicina Professor Doutor Rui Albergaria nasceu da necessidade de assegurar uma resposta de teleradiologia de elevada qualidade, suportada por um corpo clínico de topo.</p>
    <p>Os nossos médicos são sub-especializados nas diferentes áreas: sistema musculo-esquelético, medicina desportiva, neurorradiologia, abdómen, pélvis, sistema cardiovascular e mama.Todos os nossos exames recebem assim uma consultadoria diferenciada por especialistas de renome, assegurando o máximo rigor diagnóstico.</p>
  </div>
  <div class="abs diagram" role="img" aria-label="Ilustração da rede de teleradiologia: centro de serviço, hospital requisitante e radiologista"></div>
  <div class="abs btn teal" style="top:330px">Os melhores Médicos</div>
  <div class="abs btn navy" style="top:418px">EM LUANDA</div>
  <div class="abs btn teal" style="top:500px">Baixo custo</div>
</section>

<section class="slide profile">
  <div class="abs panel"></div>
  <div class="abs portrait" role="img" aria-label="Retrato do diretor clínico de fato escuro"></div>
  <h2 class="abs">RUI ALBERGARIA</h2>
  <h3 style="top:150px">Educação Universitária</h3>
  <p class="bio" style="top:185px">Licenciado em Medicina pela Faculdade de Ciências Médicas do Tejo (FCMT), com a classificação final de 17,17 valores (2000).Doutorado em Medicina pela FCMT, aprovado por Unanimidade com Distinção e Louvor (2012).</p>
  <h3 style="top:268px">Educação Pós-Graduada</h3>
  <p class="bio" style="top:303px">Médico Interno de Imagiologia e Radiodiagnóstico do Hospital Universitário de Vale Verde (2003 a 2008).Visiting Clinical Fellow – Vascular Imaging, Pacific Coast Medical University (2008).Visiting Clinical Fellow – Musculoskeletal Imaging, Service de Radiologie Ostéoarticulaire, Hôpital Saint-Aubin, Lyon (2008).</p>
  <h3 style="top:413px">Funções Actuais</h3>
  <p class="bio" style="top:450px">CEO, Centro de Telemedicina (desde 2013). Membro da Comissão Editorial do “Global Review of Orthopaedic Imaging” (desde 2014). Grau de Consultor (Imagiologia) pelo Colégio Nacional de Médicos (desde 2018). Professor Auxiliar Convidado e Regente de Disciplina do Instituto Médico Atlântico (desde 2018). Investigador do Centro de Investigação em Saúde Integrada, CISI/IMA (desde 2018).</p>
</section>

<section class="slide services">
  <div class="abs" role="img" aria-label="Fundo escurecido de ambiente clínico" style="inset:0;background:radial-gradient(ellipse at 30% 20%,rgba(80,90,100,.25),transparent 60%)"></div>
  <h2 class="abs">FORNECEMOS</h2>
  <div class="card" style="left:112px;top:192px"><span class="num">1</span>Intervenção por especialistas de topo</div>
  <div class="card" style="left:428px;top:192px"><span class="num">2</span>Análise sub-especializada de todos os exames</div>
  <div class="card" style="left:745px;top:192px"><span class="num">3</span>Necessidades ocasionais ou permanentes</div>
  <div class="card" style="left:271px;top:406px"><span class="num">4</span>Cobertura diurna e nocturna</div>
  <div class="card" style="left:587px;top:406px"><span class="num">5</span>Âmbito Internacional</div>
</section>

<section class="slide costs">
  <div class="abs dots" role="img" aria-label="Padrão decorativo de pontos" style="left:20px;top:30px"></div>
  <div class="abs band">CUSTOS CONTROLADOS</div>
  <ul>
    <li><svg width="12" height="12" viewBox="0 0 12 12"><circle cx="6" cy="6" r="6" fill="#1e3a6b"/><path d="M5 3.5 7.5 6 5 8.5" stroke="#fff" stroke-width="1.5" fill="none"/></svg>Despesa com a montagem da plataforma informática fica completamente do nosso lado</li>
    <li><svg width="12" height="12" viewBox="0 0 12 12"><circle cx="6" cy="6" r="6" fill="#1e3a6b"/><path d="M5 3.5 7.5 6 5 8.5" stroke="#fff" stroke-width="1.5" fill="none"/></svg>Não existe qualquer pagamento inicial</li>
    <li><svg width="12" height="12" viewBox="0 0 12 12"><circle cx="6" cy="6" r="6" fill="#1e3a6b"/><path d="M5 3.5 7.5 6 5 8.5" stroke="#fff" stroke-width="1.5" fill="none"/></svg>Não existem quaisquer custos fixos ou um mínimo de exames obrigatório</li>
    <li><svg width="12" height="12" viewBox="0 0 12 12"><circle cx="6" cy="6" r="6" fill="#1e3a6b"/><path d="M5 3.5 7.5 6 5 8.5" stroke="#fff" stroke-width="1.5" fill="none"/></svg>Temos simplesmente um preço por relatório</li>
    <li><svg width="12" height="12" viewBox="0 0 12 12"><circle cx="6" cy="6" r="6" fill="#1e3a6b"/><path d="M5 3.5 7.5 6 5 8.5" stroke="#fff" stroke-width="1.5" fill="none"/></svg>São faturados apenas os relatórios efectivados</li>
  </ul>
  <div class="abs dots" role="img" aria-label="Padrão decorativo de pontos" style="left:402px;top:548px"></div>
  <div class="abs photo" role="img" aria-label="Equipa médica reunida à mesa a rever documentos"></div>
</section>

<section class="slide closing">
  <svg class="abs" style="left:0;top:0" width="1128" height="635" viewBox="0 0 1128 635" aria-hidden="true"><polygon points="0,0 399,0 538,635 0,635" fill="#1e3a6b"/></svg>
  <div class="abs frame"></div>
  <div class="abs ring"></div>
  <div class="abs photo" role="img" aria-label="Retrato de médico sorridente de bata branca"></div>
  <h2 class="abs">SOBRE NÓS</h2>
</section>

</body>
</html>
```